Veteran Owned General Contractor needs Bold New Business Cards

We are a service disabled veteran owned small business. We're a general contractor that specializes in excavation, underground utilities, site work, land clearing and demolition. We would like a fresh, simple, bold, new look for our business cards. We're open to ideas! We'd like to incorporate the following information on the card:

Company Name & Logo, Name of Person, Job Title, Office Phone, Fax, Cell Phone, Email Address, Website, SDVOSB

Our logo is included. We look forward to your thoughts.

Thank you!
Updates

Reason: Hello Due to the overwhelming response to this project, we are extending the deadline one time to allow for improved communication and feedback with the top candidates. We would like to thank everyone for their hard work and exceptional creativity! Thank you

Industry/Entity Type

Business

Contact Information for Business Card

Font styles to use
Sans Serif

Requirements
Nice to have
• As we are a veteran owned company, it would be nice to incorporate an American flag into the design. Maybe on the back?

```html
<!DOCTYPE html>
<html lang="en">
<head>
<meta charset="utf-8">
<title>Keystone7 Inc – Business Card</title>
<link rel="stylesheet" href="https://fonts.googleapis.com/css2?family=Open+Sans:wght@400;600;700&family=Oswald:wght@500&display=swap">
<style>
  :root{
    --backdrop:#2e1d15;
    --card:#ffffff;
    --black:#050708;
    --grey:#888a8c;
    --green:#72c144;
    --ink:#111111;
    --flag-red:#b8243a;
    --flag-blue:#3c3b6e;
  }
  *{margin:0;padding:0;box-sizing:border-box}
  html,body{width:1200px;height:1000px;overflow:hidden}
  body{background:var(--backdrop);position:relative;font-family:"Open Sans",Arial,sans-serif;color:var(--ink)}
  .card{position:absolute;top:241px;width:310px;height:545px;background:var(--card);overflow:hidden;box-shadow:0 2px 4px rgba(0,0,0,.45)}
  .card--front{left:269px}
  .card--back{left:611px}

  .front-header{position:absolute;left:0;top:0;width:310px;height:240px}
  .front-brand{position:absolute;left:0;top:66px;width:310px;text-align:center;font-weight:700;font-size:34px;color:var(--green);letter-spacing:1px}

  .person{position:absolute;left:33px;top:245px}
  .person__name{font-weight:700;font-size:21px;letter-spacing:.5px;line-height:1}
  .person__name span{color:var(--grey)}
  .person__title{font-size:14px;margin-top:6px}

  .cert-band{position:absolute;left:0;top:309px;width:310px;height:27px;background:var(--black);color:#fff;font-family:"Oswald",Arial,sans-serif;font-weight:500;font-size:14px;line-height:27px;padding-left:34px;letter-spacing:.3px}

  .contacts{position:absolute;left:33px;list-style:none;font-size:14px}
  .contacts--phones{top:360px}
  .contacts--web{top:438px}
  .contacts li{display:flex;align-items:flex-start;line-height:20px}
  .contacts--phones li{height:21.7px}
  .contacts--web li{height:19.7px}
  .contacts svg{width:13px;height:13px;margin:4px 12px 0 0;flex:none;fill:var(--ink)}
  .contacts--web li.address{height:auto;line-height:21.5px}
  .contacts--web li.address svg{margin:4px 10px 0 0}

  .flag{position:absolute;left:21px;top:0;width:267px;height:457px;background:linear-gradient(135deg,var(--flag-blue) 0%,#8a6f9a 45%,var(--flag-red) 100%)}
  .back-brand{position:absolute;left:0;top:481px;width:310px;display:flex;justify-content:center;align-items:center;gap:8px}
  .back-brand__mark{width:26px;height:26px;background:var(--grey);border-radius:3px}
  .back-brand__name{font-weight:700;font-size:25px;color:var(--green);letter-spacing:.5px}
</style>
</head>
<body>

<section class="card card--front">
  <svg class="front-header" viewBox="0 0 310 240" aria-hidden="true">
    <path d="M0,180 H310 V195 Q155,235 0,195 Z" fill="var(--grey)"/>
    <path d="M0,0 H310 V183 Q155,208 0,183 Z" fill="var(--black)"/>
  </svg>
  <div class="front-brand">KEYSTONE7</div>

  <div class="person">
    <div class="person__name">JOHN <span>DOE</span></div>
    <div class="person__title">General Manager</div>
  </div>

  <div class="cert-band">SDVOSB</div>

  <ul class="contacts contacts--phones">
    <li><svg viewBox="0 0 16 16"><path d="M4 0h8a1 1 0 0 1 1 1v14a1 1 0 0 1-1 1H4a1 1 0 0 1-1-1V1a1 1 0 0 1 1-1zm.6 1.6v11.2h6.8V1.6z"/></svg>01 234 456 7898</li>
    <li><svg viewBox="0 0 16 16"><path d="M3.6 0.5l2.3 3.2-1.4 1.6c.9 2 2.6 3.8 4.6 4.8l1.6-1.4 3.3 2.2-1.3 3.1C7.3 13.8 2 8.6 1 3z"/></svg>01 234 456 7898</li>
    <li><svg viewBox="0 0 16 16"><path d="M4 1h7l1 1v3H4zM2 6h12a1 1 0 0 1 1 1v5h-3v3H4v-3H1V7a1 1 0 0 1 1-1zm3.5 5.5v2h5v-2z"/></svg>01 234 456 7898</li>
  </ul>

  <ul class="contacts contacts--web">
    <li><svg viewBox="0 0 16 16"><path d="M1 3h14v10H1zm1.5 1.3v.6L8 8.6l5.5-3.7v-.6z"/></svg>emailaddress@domain.com</li>
    <li><svg viewBox="0 0 16 16"><path d="M8 0a8 8 0 1 0 0 16A8 8 0 0 0 8 0zm5.9 7.2h-2.7a12 12 0 0 0-1-4.9 6.5 6.5 0 0 1 3.7 4.9zM8 1.6c.7.8 1.5 2.8 1.6 5.6H6.4C6.5 4.4 7.3 2.4 8 1.6zM5.8 2.3a12 12 0 0 0-1 4.9H2.1a6.5 6.5 0 0 1 3.7-4.9zM2.1 8.8h2.7a12 12 0 0 0 1 4.9 6.5 6.5 0 0 1-3.7-4.9zM8 14.4c-.7-.8-1.5-2.8-1.6-5.6h3.2c-.1 2.8-.9 4.8-1.6 5.6zm2.2-.7a12 12 0 0 0 1-4.9h2.7a6.5 6.5 0 0 1-3.7 4.9z"/></svg>www.yourwebsite.com</li>
    <li class="address"><svg viewBox="0 0 16 16"><path d="M8 0a5.5 5.5 0 0 0-5.5 5.5C2.5 10 8 16 8 16s5.5-6 5.5-10.5A5.5 5.5 0 0 0 8 0zm0 7.8a2.3 2.3 0 1 1 0-4.6 2.3 2.3 0 0 1 0 4.6z"/></svg><span>4120 Ridgeline Road<br>Norfolk, VA 23505</span></li>
  </ul>
</section>

<section class="card card--back">
  <div class="flag" role="img" aria-label="American flag, hung vertically"></div>

  <div class="back-brand">
    <span class="back-brand__mark"></span>
    <span class="back-brand__name">KEYSTONE7 INC</span>
  </div>
</section>

</body>
</html>
```